Brevik Seasoning
Brevik Seasoning - Food
Creative Brief
Simple
Tom Halvern
President and CEO
52190 Harlow Lane Maple Ridge, OH 48977
thalvern@brevikspice.com
Brevikspice.com
Xpert Xpert

```html
<!DOCTYPE html>
<html lang="en">
<head>
<meta charset="utf-8">
<title>Brevik Seasoning – Business Card</title>
<link rel="stylesheet" href="https://fonts.googleapis.com/css2?family=Kaushan+Script&family=Lora:ital,wght@0,400;0,700;1,400&display=swap">
<style>
  :root {
    --backdrop: #e9e6df;
    --card-cream: #fbefae;
    --card-light: #fff8d2;
    --spice-red: #d9342a;
    --spice-orange: #ec7a2c;
    --herb-green: #5c8f2b;
    --ink: #2b2623;
    --ink-soft: #4a403a;
  }
  * { box-sizing: border-box; margin: 0; padding: 0; }
  html, body { width: 1200px; height: 802px; overflow: hidden; }
  body {
    background: var(--backdrop);
    display: flex; align-items: center; justify-content: center;
    font-family: "Lora", Georgia, serif;
    color: var(--ink);
  }
  .business-card {
    position: relative;
    width: 1000px; height: 572px;
    border-radius: 22px;
    overflow: hidden;
    background:
      radial-gradient(ellipse 520px 300px at 34% 60%, rgba(240,120,90,0.45), rgba(240,120,90,0) 70%),
      linear-gradient(135deg, var(--card-light) 0%, var(--card-cream) 45%, #f6e08d 100%);
    box-shadow: 0 18px 40px rgba(0,0,0,0.18);
  }
  .brand {
    position: absolute; left: 70px; top: 52px;
    display: flex; align-items: center; gap: 16px;
  }
  .brand-dot {
    width: 34px; height: 34px; border-radius: 50%;
    background: var(--spice-red);
  }
  .brand-name {
    font-weight: 700; font-size: 58px; line-height: 1;
    color: var(--ink);
  }
  .brand-rule {
    position: absolute; left: 60px; top: 148px; width: 620px; height: 14px;
  }
  .brand-rule span { display: block; height: 4px; margin-bottom: 5px; border-radius: 2px; }
  .brand-rule .rule-red { background: var(--spice-red); }
  .brand-rule .rule-green { background: var(--herb-green); width: 92%; }
  .person { position: absolute; left: 100px; top: 182px; }
  .person-name {
    font-family: "Kaushan Script", cursive;
    font-size: 48px; color: var(--herb-green); line-height: 1.1;
  }
  .person-title {
    font-size: 20px; color: var(--herb-green); margin-left: 6px;
  }
  .spice-graphic {
    position: absolute; left: 60px; top: 310px; width: 240px; height: 180px;
    border-radius: 10px;
    background: linear-gradient(150deg, #f3c27a 0%, #ef8a5a 55%, #d8573e 100%);
    opacity: 0.75;
  }
  .address {
    position: absolute; left: 640px; top: 190px;
    font-style: italic; font-size: 20px; line-height: 1.4; color: var(--ink-soft);
  }
  .contact-list {
    position: absolute; left: 580px; top: 300px;
    list-style: none;
  }
  .contact-item {
    display: flex; align-items: center; gap: 18px;
    height: 50px;
    font-style: italic; font-size: 21px; color: var(--ink-soft);
  }
  .contact-icon {
    flex: none;
    width: 34px; height: 34px; border-radius: 50%;
    background: var(--spice-orange);
    border: 3px solid var(--spice-red);
    display: flex; align-items: center; justify-content: center;
  }
  .contact-icon svg { width: 18px; height: 18px; }
</style>
</head>
<body>
  <article class="business-card">
    <div class="brand">
      <span class="brand-dot"></span>
      <span class="brand-name">Brevik Seasoning</span>
    </div>
    <div class="brand-rule"><span class="rule-red"></span><span class="rule-green"></span></div>

    <div class="person">
      <p class="person-name">Tom Halvern</p>
      <p class="person-title">President and CEO</p>
    </div>

    <div class="spice-graphic" role="img" aria-label="Decorative illustration of folded spice packets in warm orange and red"></div>

    <address class="address">
      52190 Harlow Lane<br>
      Maple Ridge, OH 48977
    </address>

    <ul class="contact-list">
      <li class="contact-item">
        <span class="contact-icon"><svg viewBox="0 0 24 24" fill="#fff"><path d="M6.6 10.8a15 15 0 0 0 6.6 6.6l2.2-2.2c.3-.3.7-.4 1-.2 1.1.4 2.3.6 3.6.6.6 0 1 .4 1 1V20c0 .6-.4 1-1 1A17 17 0 0 1 3 4c0-.6.4-1 1-1h3.5c.6 0 1 .4 1 1 0 1.3.2 2.5.6 3.6.1.3 0 .7-.2 1z"/></svg></span>
        555-301-0142
      </li>
      <li class="contact-item">
        <span class="contact-icon"><svg viewBox="0 0 24 24" fill="#fff"><path d="M6.6 10.8a15 15 0 0 0 6.6 6.6l2.2-2.2c.3-.3.7-.4 1-.2 1.1.4 2.3.6 3.6.6.6 0 1 .4 1 1V20c0 .6-.4 1-1 1A17 17 0 0 1 3 4c0-.6.4-1 1-1h3.5c.6 0 1 .4 1 1 0 1.3.2 2.5.6 3.6.1.3 0 .7-.2 1z"/></svg></span>
        555-302-0187
      </li>
      <li class="contact-item">
        <span class="contact-icon"><svg viewBox="0 0 24 24" fill="none" stroke="#fff" stroke-width="2.2"><rect x="3" y="6" width="18" height="12" rx="1.5"/><path d="M3 7l9 6 9-6"/></svg></span>
        thalvern@brevikspice.com
      </li>
      <li class="contact-item">
        <span class="contact-icon"><svg viewBox="0 0 24 24" fill="none" stroke="#fff" stroke-width="2"><circle cx="12" cy="12" r="9"/><path d="M3 12h18M12 3c3 3 3 15 0 18M12 3c-3 3-3 15 0 18"/></svg></span>
        Brevikspice.com
      </li>
    </ul>
  </article>
</body>
</html>
```